Semaglutide Diet

A flyer design for a weight loss program based on the peptide Semaglutide that our clinic is rolling out. Here are some very rough ideas

```html
<!DOCTYPE html>
<html lang="en">
<head>
<meta charset="UTF-8">
<title>Semaglutide Weight Loss Flyer</title>
<link rel="stylesheet" href="https://fonts.googleapis.com/css2?family=Montserrat:wght@500;600;700;800&family=Oswald:wght@600&family=Rubik:wght@900&display=swap">
<style>
  :root {
    --green: #2f7d2b;
    --blue: #1c3f8f;
    --ink: #111111;
    --white: #ffffff;
    --page: #e6e3e3;
    --tape-soft: #f3ecc4;
  }
  * { margin: 0; padding: 0; box-sizing: border-box; }
  html, body { width: 800px; height: 1200px; overflow: hidden; background: var(--page); }
  .canvas { position: relative; width: 800px; height: 1200px; }

  .flyer {
    position: absolute; left: 20px; top: 108px;
    width: 760px; height: 984px;
    background: var(--white); overflow: hidden;
    box-shadow: 0 14px 30px rgba(0,0,0,.22);
    font-family: 'Montserrat', sans-serif;
  }

  .hero-backdrop {
    position: absolute; left: 0; top: 0; width: 760px; height: 436px;
    background: linear-gradient(160deg, #f4f4f4 0%, #e4e4e2 45%, #f7f7f7 100%);
  }
  .hero-photo {
    position: absolute; left: 470px; top: 0; width: 290px; height: 511px;
    background: linear-gradient(180deg, #3a2a22 0%, #6b4a3a 18%, #d9a88b 38%, #ee9a72 58%, #e2b496 78%, #d8a88a 100%);
    clip-path: polygon(0 0, 100% 0, 100% 100%, 46% 100%, 46% 85%, 0 85%);
    z-index: 2;
  }

  .headline { position: absolute; left: 39px; z-index: 3; white-space: nowrap; }
  .headline-kicker { top: 40px; font-size: 31px; font-weight: 800; color: var(--ink); letter-spacing: -0.5px; }
  .headline-weight { top: 68px; font-family: 'Rubik', sans-serif; font-weight: 900; font-size: 104px; line-height: 1; color: var(--green); letter-spacing: -4px; }
  .headline-loss { top: 150px; font-family: 'Rubik', sans-serif; font-weight: 900; font-size: 150px; line-height: 1; color: var(--blue); letter-spacing: -9px; }
  .headline-peptide { top: 296px; font-size: 43px; font-weight: 800; color: var(--ink); letter-spacing: -1px; }
  .headline-drug { top: 346px; font-size: 50px; font-weight: 700; color: var(--green); letter-spacing: -0.5px; }

  .approval-band {
    position: absolute; left: 0; top: 436px; width: 760px; height: 75px;
    background: var(--blue); z-index: 1;
    color: var(--white); font-size: 20px; font-weight: 500;
    display: flex; align-items: center; padding-left: 39px;
  }

  .benefits {
    position: absolute; left: 0; top: 511px; width: 363px; height: 473px;
    background: var(--green); list-style: none;
  }
  .benefit {
    position: absolute; left: 39px; width: 318px;
    display: flex; gap: 19px; align-items: flex-start;
    color: var(--white); font-size: 11px; font-weight: 500; line-height: 1.3;
  }
  .benefit svg { flex: none; width: 22px; height: 22px; margin-top: 1px; }
  .benefit span { width: 277px; }

  .goals { position: absolute; left: 363px; top: 511px; width: 397px; height: 473px; }
  .goals-ask { position: absolute; left: 36px; top: 22px; font-family: 'Oswald', sans-serif; font-weight: 600; font-size: 40px; line-height: 1; color: var(--green); letter-spacing: 0.5px; }
  .goals-result { position: absolute; left: 34px; top: 60px; font-size: 70px; font-weight: 800; line-height: 1; color: var(--blue); letter-spacing: -2px; }
  .goals-rule { position: absolute; left: 37px; top: 134px; width: 54px; height: 3px; background: var(--ink); }
  .goals-lead { position: absolute; left: 37px; top: 146px; font-size: 24px; font-weight: 700; color: var(--green); }

  .goal { position: absolute; display: flex; align-items: center; gap: 14px; }
  .goal-icon { width: 52px; height: 52px; border-radius: 50%; background: var(--blue); flex: none; display: flex; align-items: center; justify-content: center; }
  .goal-icon svg { width: 30px; height: 30px; }
  .goal-label { font-size: 11.5px; font-weight: 600; line-height: 1.05; color: var(--ink); width: 96px; }

  .tape-measure {
    position: absolute; left: 218px; top: 378px; width: 150px; height: 80px;
    background: linear-gradient(135deg, var(--tape-soft) 0%, #faf7e6 100%);
  }
</style>
</head>
<body>
<div class="canvas">
  <article class="flyer">
    <div class="hero-backdrop" role="img" aria-label="Soft faded photo of a tape measure on a light background"></div>
    <div class="hero-photo" role="img" aria-label="Photo of a fit woman in an orange sports bra, hand on hip"></div>

    <p class="headline headline-kicker">A NEW VERY EFFECTIVE</p>
    <p class="headline headline-weight">WEIGHT</p>
    <p class="headline headline-loss">LOSS</p>
    <p class="headline headline-peptide">PEPTIDE</p>
    <p class="headline headline-drug">SEMAGLUTIDE</p>

    <div class="approval-band">(FDA APPROVED SLIMVORA/GLUCENTA)</div>

    <ul class="benefits">
      <li class="benefit" style="top:42px"><svg viewBox="0 0 22 22"><path d="M3 12 L9 18 L20 3" fill="none" stroke="#1c3f8f" stroke-width="3.5" stroke-linecap="round" stroke-linejoin="round"/></svg><span>ONLINE TELEHEALTH WEIGHT LOSS PROGRAM</span></li>
      <li class="benefit" style="top:109px"><svg viewBox="0 0 22 22"><path d="M3 12 L9 18 L20 3" fill="none" stroke="#1c3f8f" stroke-width="3.5" stroke-linecap="round" stroke-linejoin="round"/></svg><span>REAL WEIGHT LOSS RESULTS OF UP TO <span style="white-space:nowrap">2-4</span> POUNDS PER WEEK</span></li>
      <li class="benefit" style="top:183px"><svg viewBox="0 0 22 22"><path d="M3 12 L9 18 L20 3" fill="none" stroke="#1c3f8f" stroke-width="3.5" stroke-linecap="round" stroke-linejoin="round"/></svg><span>REDUCES APPETITE, IMPROVES CONTROL OF EATING AND REDUCES FOOD CRAVINGS</span></li>
      <li class="benefit" style="top:252px"><svg viewBox="0 0 22 22"><path d="M3 12 L9 18 L20 3" fill="none" stroke="#1c3f8f" stroke-width="3.5" stroke-linecap="round" stroke-linejoin="round"/></svg><span>IMPROVES INSULIN RESISTANCE, BURNS FAT AND BOOSTS ENERGY</span></li>
      <li class="benefit" style="top:318px"><svg viewBox="0 0 22 22"><path d="M3 12 L9 18 L20 3" fill="none" stroke="#1c3f8f" stroke-width="3.5" stroke-linecap="round" stroke-linejoin="round"/></svg><span>SAFE AND EFFECTIVE ONCE WEEKLY INJECTION</span></li>
      <li class="benefit" style="top:375px"><svg viewBox="0 0 22 22"><path d="M3 12 L9 18 L20 3" fill="none" stroke="#1c3f8f" stroke-width="3.5" stroke-linecap="round" stroke-linejoin="round"/></svg><span>CAN BE USED IN COMBINATION WITH THE ELITE PROGRAM OR IN MAINTENANCE PHASE</span></li>
    </ul>

    <section class="goals">
      <p class="goals-ask">DO YOU WANT TO</p>
      <p class="goals-result">RESULT</p>
      <div class="goals-rule"></div>
      <p class="goals-lead">Do you want to</p>

      <div class="goal" style="left:36px; top:204px">
        <div class="goal-icon"><svg viewBox="0 0 30 30" fill="none" stroke="#fff" stroke-width="1.6"><rect x="6" y="9" width="18" height="14" rx="2"/><path d="M11 13 h8 M12 16 h6 M15 5 v4"/></svg></div>
        <p class="goal-label">Lose 5 pounds or more</p>
      </div>
      <div class="goal" style="left:214px; top:204px">
        <div class="goal-icon"><svg viewBox="0 0 30 30" fill="none" stroke="#fff" stroke-width="1.6"><path d="M9 6 c-3 6 -3 13 2 18 h8 c5 -5 5 -12 2 -18"/><path d="M12 15 a3 3 0 1 1 6 0 M18 15 l-1 -2 M12 15 l1 2"/></svg></div>
        <p class="goal-label">Improve your metabolism</p>
      </div>
      <div class="goal" style="left:36px; top:290px">
        <div class="goal-icon"><svg viewBox="0 0 30 30" fill="none" stroke="#fff" stroke-width="1.6"><circle cx="12" cy="7" r="2.5"/><path d="M12 10 v9 M9 13 h6 M10 19 l-2 6 M14 19 l2 6"/><path d="M20 9 l-2 6 h3 l-2 6"/></svg></div>
        <p class="goal-label">Have more energy</p>
      </div>
      <div class="goal" style="left:214px; top:290px">
        <div class="goal-icon"><svg viewBox="0 0 30 30" fill="none" stroke="#fff" stroke-width="1.6"><circle cx="15" cy="6" r="2.5"/><path d="M9 9 l6 4 l6 -4 M15 13 v6 M11 19 h8 l-1 7 h-6 z"/></svg></div>
        <p class="goal-label">Lose water weight</p>
      </div>
      <div class="goal" style="left:36px; top:372px">
        <div class="goal-icon"><svg viewBox="0 0 30 30" fill="none" stroke="#fff" stroke-width="1.6"><path d="M15 23 c-6 -4 -10 -8 -10 -12 a5 5 0 0 1 10 -1 a5 5 0 0 1 10 1 c0 4 -4 8 -10 12 z"/><path d="M8 14 h4 l2 -3 l2 5 l2 -2 h4"/></svg></div>
        <p class="goal-label">Improve overall health</p>
      </div>

      <div class="tape-measure" role="img" aria-label="Photo of a yellow tape measure"></div>
    </section>
  </article>
</div>
</body>
</html>
```